Design Creative Banner or Gif Ads. 3 Designs To Be Selected

Come up with some creative banner ads for stonewell.co.nz

*At least 3 different winning banners will be chosen*

Please provide banner ads / gif ads in common google ads / website banner formats.

They can be gif or static but must stand out while still maintaining clear clean text and visuals, with a premium professional feel (please avoid clip art or anything that gives a cheap message).

Please keep in mind that these will likely be small ads so text needs to be large and if there's there a lot of text then use multiple frames/ pages as submit as a gif.

Style
Minimal & clean lines
Architectural or realistic images
Avoid cartoon styles, clipart, or anything that looks cheap

Font
Nexa or Montserrat or similar

Tone
Premium, serious, trustworthy — fits new builds

Colours
Option 1: Deep Navy (trust & quality) & lighter blues and warm grey
Option 2: Open to bright colours to help the ads stand out, such as (but not limited to) bright pink with black, yellow, fluorescent green, provided the messaging is still done professionally.
Our logo is attached (Stone Well Logo)

Display Sizes
Ad specs for file sizes should be file formats like JPEG, GIF, and PNG, with animations limited to a max of 30 seconds or less.
We will need several different ad sizes provided for each of the 3 selected winning designs.

• Medium Rectangle: 300 × 250 pixels
• Leaderboard: 728 × 90 pixels
• Desktop Banner ad image: (640x360 pixels)
• Desktop Banner ad image 2: (300x600 pixels)
• Possibly one or two other sizes

Flexibility to be creative
The ad text, words, upper/lower case, layout, colour, theme, and images can be adjusted to how you think it will look best. The follow example ads are just examples of what we are after but we are keen to see what you can create.

Recommendations at this point:
1. Avoid text heavy
2. Looking for more Gif ads
3. Imaging: if possible use real stock photo's rather than AI

Themes:

1
Building Soon? Start Here
Free Build Planning Pack:
✓ Build Cost Calculator
✓ Hidden Cost Checklist
✓ Builder Comparison Guide
Build With Confidence
Download Free

2
Before You Choose A Builder
Compare Price, Scope, Risk & Value
Avoid Costly Mistakes
Choose The Right Builder With Confidence
Download The Free Guide

3
Planning A New Build?
Avoid These Common Mistakes:
✗ Hidden Exclusions
✗ Missing Scope
✗ Unrealistic Allowances
✗ Budget Blowouts
Download The Free Guide

4
Before You Buy Land
Know what it could cost to build.
Avoid Costly Building Mistakes
Download Our Free Guides

5
Know Your Build Budget?
• Free Build Cost Calculator
• Hidden Cost Checklist
• Build Planning Tools
Calculate Costs (Download)

Target Market(s)

Landowners looking to build

Industry/Entity Type

Building

Font styles to use
Other font styles liked:
• Nexa or Montserrat or similar

Requirements
Should not have
• Avoid cartoon styles, clipart, or anything that looks cheap

```html
<!DOCTYPE html>
<html lang="en">
<head>
<meta charset="utf-8">
<title>Banner Ad Set</title>
<link href="https://fonts.googleapis.com/css2?family=Bebas+Neue&family=Inter:wght@400;500;600;700&display=swap" rel="stylesheet">
<style>
  :root {
    --page: #ffffff;
    --label: #333333;
    --white: #ffffff;
    --green: #7cb82f;
    --green-dark: #6aa226;
  }
  * { box-sizing: border-box; margin: 0; padding: 0; }
  html, body { width: 1050px; height: 1200px; overflow: hidden; }
  body {
    position: relative;
    background: radial-gradient(circle at 260px 220px, #f1f1f1 0, #f8f8f8 180px, var(--page) 300px);
    font-family: "Inter", Arial, sans-serif;
    color: var(--white);
  }
  .size-label {
    position: absolute; left: 100px;
    font-size: 12px; color: var(--label); font-weight: 400;
  }
  .ad { position: absolute; overflow: hidden; }
  .photo { position: absolute; inset: 0; }
  .headline {
    font-family: "Bebas Neue", "Arial Narrow", sans-serif;
    font-weight: 400; line-height: 1; letter-spacing: 0.2px;
  }
  .accent { color: var(--green); }
  .btn {
    position: absolute; display: flex; align-items: center; justify-content: center;
    gap: 10px; border-radius: 6px; font-weight: 500;
  }
  .btn--green { background: var(--green); color: var(--white); }
  .btn--white { background: var(--white); color: var(--green-dark); }
  .icon { fill: currentColor; flex: none; }

  /* Medium rectangle */
  .ad--rect { left: 101px; top: 104px; width: 300px; height: 250px; }
  .ad--rect .photo {
    background: linear-gradient(180deg, #2c8fc9 0%, #1f6ea3 40%, #184a6e 75%, #11324c 100%);
  }
  .rect__title { position: absolute; top: 25px; width: 100%; text-align: center; font-size: 46px; }
  .rect__sub {
    position: absolute; top: 70px; width: 100%; text-align: center;
    font-size: 14.5px; font-weight: 500; line-height: 22px;
  }
  .rect__feature {
    position: absolute; top: 151px; width: 100%; display: flex; justify-content: center;
    align-items: center; gap: 12px; font-size: 14.5px; font-weight: 500;
  }
  .rect__btn { left: 79px; top: 183px; width: 142px; height: 42px; font-size: 15px; }

  /* Leaderboard */
  .ad--leader { left: 101px; top: 449px; width: 728px; height: 90px; }
  .ad--leader .photo {
    background: linear-gradient(90deg, #0a1e30 0%, #143a5a 45%, #1c4e72 70%, #0d2538 100%);
  }
  .leader__title { position: absolute; left: 22px; top: 15px; font-size: 38px; }
  .leader__btn { left: 218px; top: 13px; width: 100px; height: 29px; font-size: 11px; border-radius: 3px; gap: 8px; }
  .leader__pack {
    position: absolute; left: 332px; top: 10px;
    font-size: 11.5px; font-weight: 700; line-height: 18px; letter-spacing: 0.2px;
  }
  .leader__list {
    position: absolute; top: 9px; list-style: none;
    font-size: 9.5px; line-height: 18px; font-weight: 500;
  }
  .leader__list li::before { content: "•"; margin-right: 7px; }
  .leader__list--a { left: 447px; }
  .leader__list--b { left: 582px; }
  .leader__tag { position: absolute; left: 22px; top: 57px; font-size: 12px; font-weight: 500; }
  .leader__band {
    position: absolute; left: 364px; top: 54px; width: 364px; height: 36px;
    background: var(--green);
    clip-path: polygon(12px 0, 100% 0, 100% 100%, 0 100%);
    display: flex; align-items: center; padding-left: 20px;
    font-size: 12.5px; font-weight: 700;
  }
  .leader__rule { position: absolute; left: 0; bottom: 0; width: 100%; height: 2px; background: var(--green); }

  /* Desktop banner */
  .ad--desktop { left: 101px; top: 637px; width: 640px; height: 360px; }
  .ad--desktop .photo {
    background:
      linear-gradient(180deg, rgba(20,30,42,0.95) 0%, rgba(35,50,66,0.6) 30%, rgba(70,52,30,0.55) 55%, rgba(30,42,24,0.9) 80%, #111a10 100%),
      linear-gradient(90deg, #2a3a2a, #4a3a24 50%, #2a3a2a);
  }
  .desk__title { position: absolute; left: 33px; top: 26px; font-size: 64px; }
  .desk__side {
    position: absolute; left: 351px; top: 28px;
    font-size: 18px; font-weight: 600; line-height: 27px;
  }
  .desk__rule { position: absolute; left: 350px; top: 91px; width: 290px; height: 1px; background: rgba(255,255,255,0.35); }
  .desk__sub { position: absolute; top: 103px; width: 100%; text-align: center; font-size: 15px; font-weight: 500; }
  .desk__btn-guide { left: 93px; top: 278px; width: 253px; height: 43px; font-size: 14.5px; gap: 16px; }
  .desk__btn-download { left: 364px; top: 278px; width: 183px; height: 43px; font-size: 14.5px; gap: 14px; }
  .desk__foot { position: absolute; top: 331px; width: 100%; text-align: center; font-size: 14.5px; font-weight: 600; }
</style>
</head>
<body>

<svg width="0" height="0" style="position:absolute">
  <defs>
    <symbol id="icon-cloud" viewBox="0 0 24 18">
      <path d="M19.4 7.2A7 7 0 0 0 6.3 5.3 5.5 5.5 0 0 0 6 16.3h13a4.6 4.6 0 0 0 .4-9.1ZM12 14.5 7.8 10.3h2.7V6.5h3v3.8h2.7Z"/>
    </symbol>
    <symbol id="icon-tree" viewBox="0 0 20 18">
      <rect x="7" y="0" width="6" height="5" rx="1"/>
      <rect x="9.2" y="5" width="1.6" height="3"/>
      <rect x="2.5" y="7.5" width="15" height="1.6"/>
      <rect x="2.5" y="7.5" width="1.6" height="4"/>
      <rect x="9.2" y="7.5" width="1.6" height="4"/>
      <rect x="15.9" y="7.5" width="1.6" height="4"/>
      <rect x="0" y="11.5" width="6" height="5" rx="1"/>
      <rect x="7" y="11.5" width="6" height="5" rx="1"/>
      <rect x="14" y="11.5" width="6" height="5" rx="1"/>
    </symbol>
  </defs>
</svg>

<p class="size-label" style="top:65px">Medium Rectangle: 300 × 250 pixels</p>
<section class="ad ad--rect">
  <div class="photo" role="img" aria-label="Modern two-storey house at dusk with lit windows under a blue sky"></div>
  <h2 class="headline rect__title">Bought Land?</h2>
  <p class="rect__sub">Understand The Steps To Building<br>Your New Home</p>
  <p class="rect__feature"><svg class="icon" width="18" height="16"><use href="#icon-tree"/></svg>Free Build Roadmap</p>
  <a class="btn btn--green rect__btn"><svg class="icon" width="20" height="15"><use href="#icon-cloud"/></svg>Download</a>
</section>

<p class="size-label" style="top:410px">Leaderboard: 728 × 90 pixels</p>
<section class="ad ad--leader">
  <div class="photo" role="img" aria-label="Dark evening view of a new home and driveway"></div>
  <h2 class="headline leader__title">Bought <span class="accent">Land?</span></h2>
  <a class="btn btn--green leader__btn"><svg class="icon" width="14" height="11"><use href="#icon-cloud"/></svg>Download</a>
  <p class="leader__pack">FREE BUILD<br>PLANNING PACK</p>
  <ul class="leader__list leader__list--a"><li>Build Cost Calculator</li><li>Hidden Cost Checklist</li></ul>
  <ul class="leader__list leader__list--b"><li>Build Journey Roadmap</li></ul>
  <p class="leader__tag">Avoid Costly Build Mistakes. Discover The Hidden Costs</p>
  <p class="leader__band">Choose The Right Builder With Clarity &amp; Confidence.</p>
  <div class="leader__rule"></div>
</section>

<p class="size-label" style="top:598px">Desktop Banner ad image: (640x360 pixels)</p>
<section class="ad ad--desktop">
  <div class="photo" role="img" aria-label="Single-storey home at night with warm garden lighting, trees and a stone path"></div>
  <h2 class="headline desk__title">Bought <span class="accent">Land?</span></h2>
  <p class="desk__side">Before You Choose A Builder,<br>Read This.</p>
  <div class="desk__rule"></div>
  <p class="desk__sub">Avoid Costly Mistakes, Budget Blowouts, &amp; Contract Surprises.</p>
  <a class="btn btn--white desk__btn-guide"><svg class="icon" width="18" height="16"><use href="#icon-tree"/></svg>Free Build Planning Guide</a>
  <a class="btn btn--green desk__btn-download"><svg class="icon" width="20" height="15"><use href="#icon-cloud"/></svg>Download Now</a>
  <p class="desk__foot">Choose The Right Builder With Clarity &amp; Confidence.</p>
</section>

</body>
</html>
```